Tidewell Oyster-new seafood raw bar restaurant menu

We are a Local Seafood & Raw Bar restaurant that is looking to open in 3 months. I need-Dinner Menu Design, Happy Hour Menu, Cocktail Menu, Brunch Menu, Lunch Menu. I'd like to have you start w/ the dinner menu first then whomever I choose will also do the rest of my menus. The SHELLHOUSE by Kelpcove menu is the direction im going for as far as font organization. Id like you to give us our own personal touch. Ive also provided a mock menu that a local designer started that can't finish due to timing.

Target Market(s)

mid to high end casual seafood restaurant

Industry/Entity Type

restaurant

Font styles to use
Serif
Sans Serif

Colors
0054AA
0677BA
7BADD7
CADEEF
E8F1F8
0094D4
00A9DD
6FCCEA
C7EBF8
E9F6FB
00AB8E
00BBA5
67D7C9
C6EFE9
E9F9F6

Requirements
Must have
• 11" x 14" size

```html
<!DOCTYPE html>
<html lang="en">
<head>
<meta charset="utf-8">
<title>Tidewell Oyster – Dinner Menu</title>
<link href="https://fonts.googleapis.com/css2?family=Alfa+Slab+One&family=Montserrat:wght@400;700;800&display=swap" rel="stylesheet">
<style>
  :root{
    --navy:#1d4c8e;
    --ink:#2a2a2a;
    --teal:#67c8d3;
    --teal-soft:#c6efe9;
    --paper:#ffffff;
  }
  *{margin:0;padding:0;box-sizing:border-box}
  html,body{width:943px;height:1200px;overflow:hidden;background:var(--paper)}
  .menu{position:relative;width:943px;height:1200px;font-family:"Montserrat",sans-serif;color:var(--ink)}
  .frame{position:absolute;left:0;top:0}
  .heading{position:absolute;font-family:"Alfa Slab One",serif;color:var(--navy);line-height:1;white-space:nowrap;letter-spacing:.5px}
  .item{position:absolute;width:240px}
  .dish{display:block;font-weight:800;font-size:13px;line-height:16px;color:var(--ink);white-space:nowrap}
  .note{display:block;font-size:10px;line-height:12.5px;color:var(--ink)}
  .price{position:absolute;left:338px;font-weight:800;font-size:10.5px;line-height:16px;color:var(--ink)}
  .price.big{font-size:13.5px}
  .row{position:absolute;left:120px;font-size:10px;line-height:13px}
  .rope-v{position:absolute;width:0;border-left:3px dotted #333}
  .rope-h{position:absolute;height:0;border-top:3px dotted #333}
  .kid{position:absolute;left:663px;font-weight:800;font-size:11.5px;line-height:14px}
  .brand{font-family:"Montserrat",sans-serif;font-weight:800;font-size:7px;fill:var(--navy);letter-spacing:.3px}
</style>
</head>
<body>
<main class="menu">

  <svg class="frame" width="943" height="1200" viewBox="0 0 943 1200" aria-hidden="false">
    <path d="M56,110 L66,110 Q80,40 150,38 L335,38 Q405,40 418,110 L428,110 L428,632 L418,632 Q405,704 335,706 L150,706 Q80,704 66,632 L56,632 Z" fill="none" stroke="var(--teal)" stroke-width="6"/>
    <path d="M64,118 L72,118 Q86,48 152,46 L333,46 Q399,48 412,118 L420,118 L420,624 L412,624 Q399,696 333,698 L152,698 Q86,696 72,624 L64,624 Z" fill="none" stroke="var(--teal)" stroke-width="2"/>
    <rect x="74" y="62" width="105" height="78" rx="20" fill="var(--teal-soft)" opacity=".6" role="img" aria-label="Scrolled flourish ornament"/>
    <rect x="304" y="62" width="105" height="78" rx="20" fill="var(--teal-soft)" opacity=".6" role="img" aria-label="Scrolled flourish ornament"/>
    <rect x="74" y="604" width="105" height="78" rx="20" fill="var(--teal-soft)" opacity=".6" role="img" aria-label="Scrolled flourish ornament"/>
    <rect x="304" y="604" width="105" height="78" rx="20" fill="var(--teal-soft)" opacity=".6" role="img" aria-label="Scrolled flourish ornament"/>
    <circle cx="242" cy="91" r="29" fill="none" stroke="var(--navy)" stroke-width="1.5"/>
    <text class="brand" x="242" y="89" text-anchor="middle">TIDEWELL</text>
    <text class="brand" x="242" y="98" text-anchor="middle">OYSTER</text>
  </svg>

  <!-- Raw bar -->
  <h1 class="heading" style="left:0;width:485px;text-align:center;top:134px;font-size:37px">RAW BAR</h1>
  <h2 class="heading" style="left:0;width:485px;text-align:center;top:174px;font-size:17px">CHILLED SEAFOOD</h2>

  <div class="item" style="left:120px;top:217px"><span class="dish">Oyster chef’s preparation</span></div>
  <span class="price" style="top:215px">22$</span>

  <div class="item" style="left:120px;top:243px"><span class="dish">Oyster selection</span></div>
  <span class="row" style="top:259px">House</span><span class="price" style="top:257px">22$</span>
  <span class="row" style="top:272px">East Coast</span><span class="price" style="top:271px">22$</span>
  <span class="row" style="top:285px">Regional</span><span class="price" style="top:284px">22$</span>
  <span class="row" style="top:298px">Accompaniments, top’em</span>

  <div class="item" style="left:120px;top:322px"><span class="dish">Seafood Tower</span></div>
  <span class="row" style="top:337px">Small</span><span class="price" style="top:336px">22$</span>
  <span class="row" style="top:350px">Large</span><span class="price" style="top:349px">22$</span>
  <span class="row" style="top:364px">Build Your own</span><span class="price" style="top:363px">22$</span>

  <div class="item" style="left:120px;top:387px;width:220px"><span class="dish">Ceviche</span><span class="note">Citrus, fruit, peppers, onion, cilantro</span></div>
  <span class="price" style="top:385px">22$</span>

  <div class="item" style="left:120px;top:426px;width:220px"><span class="dish">Tuna Poke/crudo</span><span class="note">Ponzu, scallions, ginger, avocado, sesame</span></div>
  <span class="price" style="top:424px">22$</span>

  <div class="item" style="left:120px;top:465px;width:220px"><span class="dish">Scallop Crudo</span><span class="note">Lemon, ginger, chives, olive oil, pine nuts</span></div>
  <span class="price" style="top:463px">22$</span>

  <div class="item" style="left:120px;top:504px"><span class="dish">Peel and eat shrimp</span><span class="note">Remoulade, tartar, cocktail</span></div>
  <span class="price big" style="top:504px">22$</span>

  <div class="item" style="left:120px;top:543px"><span class="dish">Local Fish Crudo</span><span class="note">Seasonal accompaniments</span></div>
  <span class="price big" style="top:543px">22$</span>

  <div class="item" style="left:120px;top:582px"><span class="dish">Cured Salmon</span></div>
  <span class="price big" style="top:582px">22$</span>

  <!-- Signatures -->
  <h2 class="heading" style="left:563px;top:81px;font-size:34px">SIGNATURES</h2>
  <div class="rope-v" style="left:523px;top:112px;height:552px"></div>
  <div class="rope-h" style="left:523px;top:661px;width:293px"></div>

  <div class="item" style="left:563px;top:139px"><span class="dish">Clam Linguini</span><span class="note">Local Pasta. Local Bacon, peppers, butter, herbs</span></div>
  <div class="item" style="left:563px;top:179px"><span class="dish">Vegetable Gnocchi</span><span class="note">Squash, shallots, peas, mushroom, basil,<br>parmesan</span></div>
  <div class="item" style="left:563px;top:229px"><span class="dish">Pan Seared Scallops</span><span class="note">Curry, cauliflower, carrots, eggplant, Carolina<br>gold rice</span></div>
  <div class="item" style="left:563px;top:281px"><span class="dish">Halibut Gumbo</span><span class="note">Shrimp, scallions, okra garnish</span></div>
  <div class="item" style="left:563px;top:319px"><span class="dish">Grilled Steak</span><span class="note">Roasted rainbow carrots, mashed potatoes,<br>ancho demi, chimichurri</span></div>
  <div class="item" style="left:563px;top:371px"><span class="dish">Surf and Turf Filet</span><span class="note">Asparagus, baby potatoes, bearnaise, demi<br>Fresh Catch</span></div>
  <div class="item" style="left:563px;top:422px"><span class="dish">Crab Legs</span><span class="note">Butter, cocktail, spicy remoulade</span></div>
  <div class="item" style="left:563px;top:461px"><span class="dish">Lowcountry Boil</span><span class="note">Shrimp, sausage, corn, potato</span></div>
  <div class="item" style="left:563px;top:500px"><span class="dish">Smash Burger</span><span class="note">Spicy “thousand Island”, pickles, house cut<br>fries, LTO</span></div>
  <div class="item" style="left:563px;top:551px"><span class="dish">Lobster Roll</span><span class="note">Lots of Lobstah, scallions, celery, house fries</span></div>
  <div class="item" style="left:563px;top:590px"><span class="dish">Fish Sandwich</span><span class="note">Double stacked halibut, pickled carrots,<br>Lemon/caper/dill aioli, lettuce, tomato</span></div>

  <!-- Smaller -->
  <h2 class="heading" style="left:0;width:626px;text-align:center;top:760px;font-size:34px">SMALLER</h2>

  <div class="item" style="left:55px;top:831px"><span class="dish">Fried Shrimp</span><span class="note">Remoulade</span></div>
  <div class="item" style="left:55px;top:869px"><span class="dish">Mussels</span><span class="note">Local bacon, shallot, garlic, tomato, spicy<br>herb butter</span></div>
  <div class="item" style="left:55px;top:917px"><span class="dish">Roasted Oysters</span><span class="note">½ dozen, Choice of Rockefeller, Bienville,<br>Tidewell special</span></div>
  <div class="item" style="left:55px;top:966px"><span class="dish">Shrimp and Grits</span><span class="note">Local andouille, roasted peppers, garlic,<br>shallot, charred tomato</span></div>
  <div class="item" style="left:55px;top:1015px"><span class="dish">Crab Mac’n cheese</span><span class="note">Cheddar, fontina, cotija, local pasta shells</span></div>
  <div class="item" style="left:55px;top:1063px"><span class="dish">Shrimp Remoulade</span><span class="note">Avocado, fried green tomato</span></div>

  <div class="item" style="left:325px;top:831px;width:260px"><span class="dish">Pumpkin Risotto</span><span class="note">Herbs, dried cherry, local mushrooms</span></div>
  <div class="item" style="left:325px;top:869px;width:260px"><span class="dish">Caeser</span><span class="note">Baby gem lettuce, parmesan</span></div>
  <div class="item" style="left:325px;top:917px;width:260px"><span class="dish">Upright Greens crisp greens salad</span><span class="note">Fig, goat cheese, spiced pepitos, sour cherry<br>vinaigrette</span></div>
  <div class="item" style="left:325px;top:966px;width:260px"><span class="dish">Clam Chowder</span><span class="note">New England style</span></div>
  <div class="item" style="left:325px;top:1015px;width:260px"><span class="dish">Baja Fish Tacos</span><span class="note">Slaw, cilantro, lime</span></div>
  <div class="item" style="left:325px;top:1063px;width:260px"><span class="dish">Steak Taco</span><span class="note">Mojo, dried chili salsa, pickled onion, cotija</span></div>

  <!-- Kids & desserts -->
  <div class="rope-v" style="left:607px;top:740px;height:388px"></div>
  <div class="rope-h" style="left:607px;top:1125px;width:294px"></div>

  <h2 class="heading" style="left:660px;top:736px;font-size:32px">KIDS MENU</h2>
  <span class="kid" style="top:796px">Chicken tenders</span>
  <span class="kid" style="top:830px">Mac n cheese</span>
  <span class="kid" style="top:864px">Fried Fish</span>
  <span class="kid" style="top:898px">Fried Shrimp</span>

  <h2 class="heading" style="left:660px;top:951px;font-size:32px">DESSERTS</h2>
  <span class="kid" style="top:1012px">Chocolate</span>
  <span class="kid" style="top:1046px">Raspberry</span>
  <span class="kid" style="top:1080px">blue</span>

</main>
</body>
</html>
```